RK Bastone Construction Inc.

Design a new business card for our construction company
To be removed from current card:
Delete 25 years
Delete Tenant fit up Renovations section

```html
<!DOCTYPE html>
<html lang="en">
<head>
<meta charset="utf-8">
<title>RK Bastone Construction Inc. – Business Card</title>
<link href="https://fonts.googleapis.com/css2?family=Montserrat:wght@400;700;800&display=swap" rel="stylesheet">
<style>
  :root {
    --backdrop: #9a9a9a;
    --card: #181818;
    --purple: #5b3579;
    --teal: #237a6e;
    --ink-light: #f2f2f2;
  }
  * { margin: 0; padding: 0; box-sizing: border-box; }
  html, body {
    width: 1200px;
    height: 1059px;
    overflow: hidden;
    background: var(--backdrop);
    font-family: "Montserrat", sans-serif;
  }
  .canvas {
    position: relative;
    width: 1200px;
    height: 1059px;
  }
  .card {
    position: absolute;
    left: 288px;
    width: 624px;
    height: 358px;
    border-radius: 30px;
    background: var(--card);
    text-align: center;
  }
  .card--front { top: 135px; }
  .card--back  { top: 565px; }

  .wordmark {
    position: absolute;
    left: 0;
    right: 0;
    color: var(--teal);
    font-weight: 800;
    line-height: 1;
  }
  .card--front .wordmark { top: 34px; }
  .card--back .wordmark  { top: 134px; }
  .wordmark__line { display: block; }
  .wordmark__main {
    font-size: 60px;
    letter-spacing: 2px;
  }
  .wordmark__sub {
    margin-top: 10px;
    font-size: 27px;
    letter-spacing: 9px;
  }

  .contact {
    position: absolute;
    top: 186px;
    left: 0;
    right: 0;
    color: var(--ink-light);
    font-size: 15.5px;
    font-weight: 400;
  }
  .contact__name {
    font-size: 22px;
    font-weight: 800;
    letter-spacing: 0.5px;
    line-height: 28px;
  }
  .contact__first { color: var(--purple); }
  .contact__last  { color: var(--teal); }
  .contact__cell { line-height: 24px; margin-bottom: 16px; }
  .contact__line { line-height: 23.5px; }
</style>
</head>
<body>
<main class="canvas">
  <section class="card card--front" aria-label="Business card front">
    <div class="wordmark">
      <span class="wordmark__line wordmark__main">RK BASTONE</span>
      <span class="wordmark__line wordmark__sub">CONSTRUCTION INC.</span>
    </div>
    <div class="contact">
      <p class="contact__name"><span class="contact__first">DARIO</span> <span class="contact__last">BASTONE</span></p>
      <p class="contact__cell">Cell 613-555-0148</p>
      <p class="contact__line">2180 Halden Rd., Suite 200, Ottawa, ON K1B 4R7</p>
      <p class="contact__line">Tel: 613-555-0172 ext: 114 | dario@rkbastoneconst.ca</p>
      <p class="contact__line">www.rkbastoneconstruction.ca</p>
    </div>
  </section>

  <section class="card card--back" aria-label="Business card back">
    <div class="wordmark">
      <span class="wordmark__line wordmark__main">RK BASTONE</span>
      <span class="wordmark__line wordmark__sub">CONSTRUCTION INC.</span>
    </div>
  </section>
</main>
</body>
</html>
```